ZEH Project Signage

Need a sign to be displayed in the front of properties currently under Construction or Renovation to advertise our company information. Need it to be Professional and Contemporary. We are a Design/Build Construction Company. Information should include Company Name, email, website, phone number. Attached: Logo and company brochure, also included and inspiration images

```html
<!DOCTYPE html>
<html lang="en">
<head>
<meta charset="utf-8">
<title>ZEH Construction – Project Sign</title>
<link rel="stylesheet" href="https://fonts.googleapis.com/css2?family=Montserrat:wght@500;600;700&display=swap">
<style>
  :root {
    --bg: #e5e5e5;
    --charcoal: #333333;
    --white: #ffffff;
    --ink: #111111;
    --signal-yellow: #f2e841;
  }
  * { margin: 0; padding: 0; box-sizing: border-box; }
  html, body {
    width: 1200px;
    height: 1200px;
    overflow: hidden;
    background: var(--bg);
    font-family: "Montserrat", Arial, sans-serif;
  }
  .sign {
    position: absolute;
    left: 234px;
    top: 70px;
    width: 732px;
    height: 1060px;
    background: var(--charcoal);
    box-shadow: 6px 8px 8px rgba(0, 0, 0, 0.35);
  }
  .brand-panel {
    position: absolute;
    left: 8px;
    top: 8px;
    width: 716px;
    height: 308px;
    background: var(--white);
    display: flex;
    align-items: center;
    justify-content: center;
    gap: 18px;
  }
  .brand-dot {
    width: 34px;
    height: 34px;
    border-radius: 50%;
    background: var(--signal-yellow);
  }
  .brand-name {
    font-weight: 600;
    font-size: 44px;
    letter-spacing: 2px;
    color: var(--ink);
  }
  .service-title {
    position: absolute;
    left: 0;
    top: 340px;
    width: 100%;
    height: 70px;
    text-align: center;
    font-weight: 600;
    font-size: 68px;
    letter-spacing: 4px;
    color: var(--white);
    line-height: 70px;
  }
  .divider {
    position: absolute;
    left: 8px;
    top: 440px;
    width: 716px;
    height: 32px;
    background: var(--white);
  }
  .contact-icon {
    position: absolute;
    left: 50%;
    transform: translateX(-50%);
    border-radius: 50%;
    background: var(--white);
    display: flex;
    align-items: center;
    justify-content: center;
  }
  .contact-icon svg { display: block; }
  .icon-phone { top: 494px; width: 78px; height: 78px; }
  .icon-mail  { top: 668px; width: 72px; height: 72px; }
  .icon-pin   { top: 809px; width: 70px; height: 70px; }
  .contact-text {
    position: absolute;
    left: 0;
    width: 100%;
    text-align: center;
    color: var(--white);
    line-height: 1;
  }
  .phone {
    top: 580px;
    font-weight: 700;
    font-size: 76px;
    letter-spacing: -1px;
  }
  .email {
    top: 759px;
    font-weight: 600;
    font-size: 37px;
  }
  .address {
    top: 889px;
    font-weight: 500;
    font-size: 32px;
    line-height: 38px;
  }
  .web-strip {
    position: absolute;
    left: 0;
    bottom: 0;
    width: 100%;
    height: 74px;
    background: var(--white);
    display: flex;
    align-items: center;
    justify-content: center;
  }
  .website {
    font-weight: 600;
    font-size: 27px;
    letter-spacing: 2.5px;
    color: var(--charcoal);
  }
</style>
</head>
<body>
  <div class="sign">
    <div class="brand-panel">
      <span class="brand-dot"></span>
      <span class="brand-name">ZEH CONSTRUCTION</span>
    </div>

    <h1 class="service-title">DESIGN-BUILD</h1>
    <div class="divider"></div>

    <div class="contact-icon icon-phone">
      <svg width="50" height="50" viewBox="0 0 24 24" aria-hidden="true">
        <path fill="#333" d="M6.6 10.8c1.4 2.8 3.8 5.1 6.6 6.6l2.2-2.2c.3-.3.7-.4 1-.2 1.1.4 2.3.6 3.6.6.6 0 1 .4 1 1V20c0 .6-.4 1-1 1C10.6 21 3 13.4 3 4c0-.6.4-1 1-1h3.5c.6 0 1 .4 1 1 0 1.3.2 2.5.6 3.6.1.3 0 .7-.2 1L6.6 10.8z"/>
      </svg>
    </div>
    <div class="contact-text phone">555-013-2748</div>

    <div class="contact-icon icon-mail">
      <svg width="44" height="30" viewBox="0 0 44 30" aria-hidden="true">
        <rect x="2" y="2" width="40" height="26" fill="none" stroke="#333" stroke-width="3"/>
        <path d="M2 2 L22 17 L42 2 M2 28 L17 14 M42 28 L27 14" fill="none" stroke="#333" stroke-width="3"/>
      </svg>
    </div>
    <div class="contact-text email">info@zehconstruction.com</div>

    <div class="contact-icon icon-pin">
      <svg width="34" height="46" viewBox="0 0 34 46" aria-hidden="true">
        <path fill="#333" fill-rule="evenodd" d="M17 2C8.7 2 2 8.5 2 16.5c0 8 15 27.5 15 27.5s15-19.5 15-27.5C32 8.5 25.3 2 17 2zm0 7.5a7 7 0 1 1 0 14 7 7 0 0 1 0-14z"/>
      </svg>
    </div>
    <div class="contact-text address">
      1840 Harbor Line Rd. Ste. 310<br>
      Lakeview, FL 32010
    </div>

    <div class="web-strip">
      <span class="website">WWW.ZEHCONSTRUCTION.COM</span>
    </div>
  </div>
</body>
</html>
```